Postcard Design

We need a postcard design for a Michigan based company called Harbor Claim Partners. We find owners of unclaimed funds and return the funds to them. We audit government records across the county for these funds. Please visit our website at www.harborclaimpartners.example to get a better feel for what we do.
The biggest hurdle is having these people believe that this is true, that they are owed this money.

Another key element is that these people have been through a loss, these funds are the result of a Tax sale on the property that they or a family member owned. (Don't state that anywhere on the post card!) So go to the emotion(s) of what this money will mean to them and their family members. Pay off bills, pay for the kids college, pay off that car, etc. It is found, FREE money! It is their money. If we don't claim the money the government agency holding the money gets to keep it and it is lost forever!

The attached file is of a letter we use currently to direct mail people. Like to use the best parts of this letter on the post card design.

Target Market(s)

People whom may not want to be contacted, owe money to people, etc.

Industry/Entity Type

Government

Requirements
Must have
• Our 800 number and website.
That we locate unclaimed funds with no up-front cost to you.

```html
<!DOCTYPE html>
<html lang="en">
<head>
<meta charset="utf-8">
<title>Harbor Claim Partners – Postcard</title>
<link rel="stylesheet" href="https://fonts.googleapis.com/css2?family=Gelasio:wght@400;700&family=Arimo:wght@400;700&display=swap">
<style>
  :root {
    --brand-green: #1d5a12;
    --text-green: #2c7d1c;
    --note-tint-light: #f4f8f1;
    --note-tint-mid: #c9dcc3;
    --note-tint-deep: #9fbd98;
    --paper: #ffffff;
  }
  html, body {
    margin: 0;
    padding: 0;
    overflow: hidden;
    background: var(--paper);
  }
  .postcard {
    position: relative;
    width: 1200px;
    height: 930px;
    overflow: hidden;
    background: var(--paper);
  }
  .banknote-art {
    position: absolute;
    left: 270px;
    top: 500px;
    width: 930px;
    height: 400px;
  }
  .masthead {
    position: absolute;
    left: 26px;
    top: 6px;
    margin: 0;
    color: var(--brand-green);
  }
  .company-name {
    display: block;
    font-family: "Gelasio", Georgia, serif;
    font-weight: 700;
    font-size: 76px;
    line-height: 86px;
    letter-spacing: 0.5px;
  }
  .contact-line {
    display: block;
    font-family: "Gelasio", Georgia, serif;
    font-weight: 400;
    font-size: 31px;
    line-height: 34px;
    color: var(--brand-green);
  }
  .copy {
    position: absolute;
    left: 30px;
    top: 172px;
    width: 600px;
  }
  .section {
    margin: 0 0 18px 0;
  }
  .section-title {
    margin: 0;
    font-family: "Gelasio", Georgia, serif;
    font-weight: 700;
    font-size: 29px;
    line-height: 36px;
    color: var(--brand-green);
  }
  .section-body {
    margin: 0;
    font-family: "Arimo", Arial, sans-serif;
    font-weight: 400;
    font-size: 21px;
    line-height: 26px;
    color: var(--text-green);
  }
</style>
</head>
<body>
<main class="postcard">
  <svg class="banknote-art" viewBox="0 0 930 400" role="img" aria-label="Faded illustration of a hundred-dollar banknote lying at an angle">
    <defs>
      <linearGradient id="noteFade" x1="0" y1="0" x2="1" y2="0.4">
        <stop offset="0" stop-color="var(--note-tint-light)" stop-opacity="0.3"/>
        <stop offset="0.45" stop-color="var(--note-tint-mid)"/>
        <stop offset="1" stop-color="var(--note-tint-deep)"/>
      </linearGradient>
    </defs>
    <polygon points="40,30 910,60 880,390 0,320" fill="url(#noteFade)" opacity="0.75"/>
  </svg>

  <h1 class="masthead">
    <span class="company-name">Harbor Claim Partners</span>
    <span class="contact-line">http://www.harborclaimpartners.example/</span>
    <span class="contact-line">1-800-555-0142</span>
  </h1>

  <section class="copy">
    <div class="section">
      <h2 class="section-title">What we do?</h2>
      <p class="section-body">We scour the country looking for unclaimed<br>funds. We find them by auditing government<br>agencies, examining their public records and<br>identifying money they’re holding in trust for<br>&nbsp;individuals like you..</p>
    </div>
    <div class="section">
      <h2 class="section-title">How the recovery process works?</h2>
      <p class="section-body">We can assist you in the recovery of your funds<br>&nbsp;and do so on a contingency basis (that<br>means no upfront cost to you).We will NEVER<br>ask you to pay anything out-of-pocket. If<br>we’re successful in recovering these funds,<br>only then are we paid a percentage. You keep<br>the lion’s share, of course.</p>
    </div>
    <div class="section">
      <h2 class="section-title">What’s the Catch?</h2>
      <p class="section-body">No catch at all.&nbsp; If the money we found is yours,<br>we get paid a finders fee for our work.If the<br>money is not yours then we do not get paid.<br>We do not ask for any money in advance from<br>you and we only get paid if we get you money!</p>
    </div>
  </section>
</main>
</body>
</html>
```